Brazilian food stall looking for a make over

We need a new Design for the front of our stall that would look authentic, colourful and practical as we have to transport, set up and put down in few hours.
We are based in Brisbane and our business are call The Ember Stand.
We sell Brazilian traditional BBQ and vegetarians options at markets, festivals and privet functions. We are new to this business and at the moment we are using our own design as presented on the image below.
We would like to see designs that would be eye catching with high contrast for easy recognition of the product with a menu with images of the product.

Requirements
Must have
• A connection with the product that is Brazilian bbq

```html
<!DOCTYPE html>
<html lang="en">
<head>
<meta charset="utf-8">
<title>The Brazilian BBQ Feast – The Ember Stand</title>
<link rel="stylesheet" href="https://fonts.googleapis.com/css2?family=Lobster&family=Archivo+Narrow:wght@400;700&display=swap">
<style>
  :root {
    --brown-deep: #3e1a0a;
    --brown-mid: #6e3417;
    --brown-glow: #a4552a;
    --title-white: #ffffff;
    --title-shadow: rgba(40, 12, 2, 0.75);
    --menu-yellow: #ffd21f;
    --menu-white: #ffffff;
    --brand-orange: #f5a21c;
    --food-dark: #3a2418;
    --food-warm: #8a5a34;
    --plate-light: #efe9e2;
  }
  html, body {
    margin: 0;
    padding: 0;
    width: 1200px;
    height: 280px;
    overflow: hidden;
    background: var(--brown-deep);
  }
  .banner {
    position: relative;
    width: 1200px;
    height: 280px;
    overflow: hidden;
    background:
      radial-gradient(ellipse 620px 300px at 640px 90px, var(--brown-glow) 0%, var(--brown-mid) 45%, var(--brown-deep) 100%);
  }
  .dish-photo {
    position: absolute;
    left: 0;
    top: 28px;
    width: 262px;
    height: 228px;
    border-radius: 0 50% 50% 0 / 0 50% 50% 0;
    background: radial-gradient(ellipse at 55% 45%, var(--food-warm) 0%, var(--food-dark) 55%, var(--plate-light) 100%);
  }
  .title {
    position: absolute;
    margin: 0;
    font-family: "Lobster", cursive;
    font-weight: 400;
    color: var(--title-white);
    text-shadow: 3px 3px 4px var(--title-shadow);
    line-height: 1;
    white-space: nowrap;
  }
  .title-the { left: 332px; top: 26px; font-size: 58px; }
  .title-main { left: 438px; top: 18px; font-size: 86px; letter-spacing: 1px; }
  .title-feast { left: 640px; top: 128px; font-size: 96px; }
  .menu {
    position: absolute;
    left: 298px;
    top: 146px;
    font-family: "Archivo Narrow", sans-serif;
    color: var(--menu-white);
    font-size: 18px;
    line-height: 22px;
  }
  .menu p { margin: 0; }
  .menu-choice {
    color: var(--menu-yellow);
    font-weight: 700;
  }
  .brand-name {
    position: absolute;
    right: 42px;
    top: 210px;
    margin: 0;
    font-family: "Archivo Narrow", sans-serif;
    font-weight: 700;
    font-size: 26px;
    color: var(--brand-orange);
    white-space: nowrap;
  }
</style>
</head>
<body>
  <div class="banner">
    <div class="dish-photo" role="img" aria-label="Photo of a plate of grilled steak with black beans, rice, fried plantain and vinaigrette salad"></div>

    <h1 class="title title-the">The</h1>
    <p class="title title-main">Brazilian BBQ</p>
    <p class="title title-feast">Feast</p>

    <div class="menu">
      <p class="menu-choice">Choice of Beef Or Chicken</p>
      <p>Served with: Feijao preto</p>
      <p>(Black bean casserole) Arroz (Rice)</p>
      <p>Vinaigrette Salad</p>
    </div>

    <p class="brand-name">The Ember Stand</p>
  </div>
</body>
</html>
```